Velvet Crypt Mixtape Podcast Design

My audio drama podcast is a funny horror story with romantic elements called Velvet Crypt Mixtape.
I'm looking for a colorful design featuring the title and letting the viewer know this is a horror show.
The title needs to be clearly visible even in thumbnail size.

```html
<!DOCTYPE html>
<html lang="en">
<head>
<meta charset="utf-8">
<title>Velvet Crypt Mixtape – Podcast Cover</title>
<link rel="stylesheet" href="https://fonts.googleapis.com/css2?family=Roboto:ital,wght@1,900&display=swap">
<style>
  :root {
    --blood-red: #ee3237;
    --paper-white: #ffffff;
    --ink-dark: #1c1c1e;
    --shadow-dark: rgba(20, 20, 22, 0.85);
    --backdrop-deep: #2b2a2d;
    --backdrop-mid: #5d5c60;
    --backdrop-light: #8c8b8f;
  }
  html, body {
    margin: 0;
    padding: 0;
    width: 1200px;
    height: 801px;
    overflow: hidden;
    background: var(--backdrop-deep);
  }
  .cover {
    position: relative;
    width: 1200px;
    height: 801px;
    overflow: hidden;
    font-family: "Roboto", "Arial", sans-serif;
  }
  .backdrop {
    position: absolute;
    inset: 0;
    background:
      radial-gradient(ellipse 55% 45% at 50% 52%, var(--backdrop-light) 0%, var(--backdrop-mid) 45%, transparent 80%),
      linear-gradient(160deg, #3a393d 0%, var(--backdrop-deep) 60%, #1e1d20 100%);
  }
  .brand-badge {
    position: absolute;
    left: 36px;
    top: 29px;
    width: 128px;
    height: 99px;
    background: var(--paper-white);
    display: flex;
    align-items: center;
    justify-content: center;
  }
  .brand-name {
    font-weight: 900;
    font-style: italic;
    font-size: 40px;
    color: var(--ink-dark);
    letter-spacing: 1px;
  }
  .drip-band {
    position: absolute;
    background: var(--blood-red);
  }
  .drip-band--top {
    left: 360px;
    top: 150px;
    width: 552px;
    height: 56px;
  }
  .drip-band--bottom {
    left: 300px;
    top: 645px;
    width: 565px;
    height: 56px;
  }
  .title {
    position: absolute;
    inset: 0;
  }
  .title text {
    font-family: "Roboto", "Arial", sans-serif;
    font-weight: 900;
    font-style: italic;
    text-anchor: middle;
  }
  .title__shadow { fill: var(--shadow-dark); }
  .title__lead { fill: var(--blood-red); font-size: 176px; }
  .title__middle { fill: var(--paper-white); font-size: 92px; }
  .title__close {
    fill: var(--blood-red);
    font-size: 96px;
    stroke: var(--paper-white);
    stroke-width: 10px;
    paint-order: stroke fill;
    stroke-linejoin: round;
  }
</style>
</head>
<body>
  <main class="cover">
    <div class="backdrop" role="img" aria-label="Dark close-up photograph of an eye with long lashes"></div>

    <div class="brand-badge">
      <span class="brand-name">VCM</span>
    </div>

    <div class="drip-band drip-band--top" role="img" aria-label="Dripping blood border above the title"></div>

    <svg class="title" width="1200" height="801" viewBox="0 0 1200 801" aria-labelledby="show-title">
      <title id="show-title">Velvet Crypt Mixtape</title>
      <text class="title__shadow" x="632" y="393" font-size="176">VELVET</text>
      <text class="title__lead" x="620" y="383">VELVET</text>

      <text class="title__shadow" x="614" y="519" font-size="92">CRYPT</text>
      <text class="title__middle" x="608" y="513">CRYPT</text>

      <text class="title__shadow" x="606" y="633" font-size="96">MIXTAPE</text>
      <text class="title__close" x="598" y="625">MIXTAPE</text>
    </svg>

    <div class="drip-band drip-band--bottom" role="img" aria-label="Dripping blood border below the title"></div>
  </main>
</body>
</html>
```